Sleek & Sexy MedSpa Direct Mailer Needed for High End Client

We need an eye catching and elegant direct mailer for our client Corva Lune Medical Spa. Please stay with black & white tones. They like Tessa Brimlow brand looks - sleek & sexy & high end.

Here is the template layout: https://quillvane.com/offering/coupon-mailer you can download a PDF or IDML on that page.

Website: https://corvalunemedicalspa.com/
Logo: https://files.dorvex.com/folders/7kqPz3Rt9Wm2Lx8Vb4Nc6Yh1Jd5Gs0FaE

Offers:
New Year/ New You! Make your beauty dreams a reality!
15% off laser hair removal packages
$50 off Velquin or Parelle
$75 off 1 Filler syringe
15% off KX products

Call today to learn more & make sure to mention MAIL OFFER!

```html
<!DOCTYPE html>
<html lang="en">
<head>
<meta charset="utf-8">
<title>Corva Lune Medical Spa – New Year Mailer</title>
<link href="https://fonts.googleapis.com/css2?family=Great+Vibes&family=Montserrat:wght@400;500&family=Bebas+Neue&display=swap" rel="stylesheet">
<style>
  :root {
    --ink: #000000;
    --paper: #ffffff;
    --label-bg: rgba(255, 255, 255, 0.55);
    --tan: #d7ad7f;
    --silver: #e8e8e8;
    --warm-light: #f4e2cf;
    --warm-mid: #d9b99a;
    --warm-dark: #8a6548;
    --gray-light: #e4e4e4;
    --gray-mid: #b9b9b9;
    --gray-dark: #5c5c5c;
  }
  * { box-sizing: border-box; margin: 0; padding: 0; }
  html, body {
    width: 1200px; height: 584px; overflow: hidden;
    background: var(--paper);
  }
  .sheet { position: relative; width: 1200px; height: 584px; }

  .mailer {
    position: absolute; top: 0;
    width: 584px; height: 584px; overflow: hidden;
    font-family: "Montserrat", sans-serif; color: var(--ink);
  }
  .mailer--color { left: 0; --frame: var(--tan); --l: var(--warm-light); --m: var(--warm-mid); --d: var(--warm-dark); }
  .mailer--mono  { left: 616px; --frame: var(--silver); --l: var(--gray-light); --m: var(--gray-mid); --d: var(--gray-dark); }

  .mailer__photo {
    position: absolute; inset: 0;
    background:
      radial-gradient(ellipse 45% 55% at 78% 40%, var(--d) 0%, transparent 70%),
      radial-gradient(ellipse 60% 40% at 70% 92%, var(--l) 0%, transparent 70%),
      linear-gradient(90deg, var(--l) 0%, var(--l) 35%, var(--m) 75%, var(--d) 100%);
  }

  .frame { position: absolute; background: var(--frame); }
  .frame--top-left     { left: 40px;  top: 40px;  width: 112px; height: 6px; }
  .frame--side-left    { left: 40px;  top: 40px;  width: 6px;   height: 503px; }
  .frame--bottom-left  { left: 40px;  top: 537px; width: 92px;  height: 6px; }
  .frame--top-right    { left: 432px; top: 40px;  width: 111px; height: 6px; }
  .frame--side-right   { left: 537px; top: 40px;  width: 6px;   height: 503px; }
  .frame--bottom-right { left: 451px; top: 537px; width: 92px;  height: 6px; }

  .brand {
    position: absolute; left: 152px; width: 280px; top: 36px;
    text-align: center; font-weight: 500; font-size: 15px;
    letter-spacing: 0.18em; text-transform: uppercase; line-height: 1.3;
  }

  .headline {
    position: absolute; left: 66px; top: 118px;
    font-family: "Great Vibes", cursive; font-weight: 400;
    font-size: 66px; line-height: 62px;
  }
  .headline__line { display: block; }
  .headline__line--second { padding-left: 36px; }

  .tagline {
    position: absolute; left: 67px; top: 274px;
    font-size: 17px; letter-spacing: 0.3em; line-height: 22px;
    text-transform: uppercase;
  }

  .offers { position: absolute; left: 67px; top: 332px; list-style: none; }
  .offer { display: flex; height: 29px; margin-bottom: 2.4px; font-size: 16px; }
  .offer__amount {
    width: 86px; background: var(--ink); color: var(--paper);
    display: flex; align-items: center; padding-left: 6px;
  }
  .offer__item {
    margin-left: 2px; background: var(--label-bg);
    display: flex; align-items: center; padding: 0 10px;
  }

  .cta {
    position: absolute; left: 132px; top: 493px; width: 319px; height: 69px;
    background: var(--ink); color: var(--paper);
    font-family: "Bebas Neue", sans-serif; font-size: 26px; line-height: 26px;
    text-align: center; display: flex; flex-direction: column; justify-content: center;
  }
</style>
</head>
<body>
<main class="sheet">
  <section class="mailer mailer--color">
    <div class="mailer__photo" role="img" aria-label="Photo of a smiling woman in a straw hat and floral off-shoulder dress, warm beige tones"></div>
    <div class="frame frame--top-left"></div><div class="frame frame--side-left"></div><div class="frame frame--bottom-left"></div>
    <div class="frame frame--top-right"></div><div class="frame frame--side-right"></div><div class="frame frame--bottom-right"></div>
    <p class="brand">Corva Lune Medical Spa</p>
    <h1 class="headline"><span class="headline__line">New Year</span><span class="headline__line headline__line--second">New You!</span></h1>
    <p class="tagline">Make your beauty<br>dreams a reality!</p>
    <ul class="offers">
      <li class="offer"><span class="offer__amount">15% OFF</span><span class="offer__item">laser hair removal packages</span></li>
      <li class="offer"><span class="offer__amount">$50 OFF</span><span class="offer__item">Velquin or Parelle</span></li>
      <li class="offer"><span class="offer__amount">$75 OFF</span><span class="offer__item">1 Filler syringe</span></li>
      <li class="offer"><span class="offer__amount">15% OFF</span><span class="offer__item">KX products</span></li>
    </ul>
    <p class="cta"><span>Call today to learn more &amp;</span><span>make sure to mention mail offer!</span></p>
  </section>

  <section class="mailer mailer--mono">
    <div class="mailer__photo" role="img" aria-label="Black and white photo of a smiling woman in a straw hat and floral off-shoulder dress"></div>
    <div class="frame frame--top-left"></div><div class="frame frame--side-left"></div><div class="frame frame--bottom-left"></div>
    <div class="frame frame--top-right"></div><div class="frame frame--side-right"></div><div class="frame frame--bottom-right"></div>
    <p class="brand">Corva Lune Medical Spa</p>
    <h1 class="headline"><span class="headline__line">New Year</span><span class="headline__line headline__line--second">New You!</span></h1>
    <p class="tagline">Make your beauty<br>dreams a reality!</p>
    <ul class="offers">
      <li class="offer"><span class="offer__amount">15% OFF</span><span class="offer__item">laser hair removal packages</span></li>
      <li class="offer"><span class="offer__amount">$50 OFF</span><span class="offer__item">Velquin or Parelle</span></li>
      <li class="offer"><span class="offer__amount">$75 OFF</span><span class="offer__item">1 Filler syringe</span></li>
      <li class="offer"><span class="offer__amount">15% OFF</span><span class="offer__item">KX products</span></li>
    </ul>
    <p class="cta"><span>Call today to learn more &amp;</span><span>make sure to mention mail offer!</span></p>
  </section>
</main>
</body>
</html>
```